Business Card

We need a business card for a fundraising/sales and marketing company called Kelvora Appeals services. The logo colours are Red Black and white. The final design should communicate professional, reliable yet fun and charity minded
Updates

Sorry for the delay. A decision will be made in the next 48 hours. we are stuck between two designs. Kind Regards, Molly Ravenscroft

Industry/Entity Type

Marketing

```html
<!DOCTYPE html>
<html lang="en">
<head>
<meta charset="utf-8">
<title>Kelvora Appeals services – Business Card</title>
<link rel="stylesheet" href="https://fonts.googleapis.com/css2?family=Arimo:wght@400;700&family=Tinos&display=swap">
<style>
  :root {
    --backdrop: #ecebe8;
    --card-white: #ffffff;
    --panel-grey: #676767;
    --ink-dark: #3b3b3b;
    --accent-red: #e0141e;
    --text-light: #ffffff;
  }
  html, body {
    margin: 0;
    width: 1200px;
    height: 800px;
    overflow: hidden;
    background: var(--backdrop);
  }
  .canvas {
    position: relative;
    width: 1200px;
    height: 800px;
  }
  .card {
    position: absolute;
    left: 150px;
    top: 143px;
    width: 900px;
    height: 514px;
    background: var(--card-white);
    box-shadow: 0 12px 30px rgba(0,0,0,0.18);
    overflow: hidden;
  }
  .brand {
    position: absolute;
    left: 0;
    width: 470px;
    top: 232px;
    text-align: center;
    font-family: "Arimo", Arial, sans-serif;
  }
  .brand-name {
    display: inline-flex;
    align-items: center;
    gap: 12px;
    font-size: 36px;
    font-weight: 400;
    letter-spacing: 1px;
    color: var(--ink-dark);
    text-transform: uppercase;
  }
  .brand-dot {
    width: 16px;
    height: 16px;
    border-radius: 50%;
    background: var(--accent-red);
  }
  .band-narrow {
    position: absolute;
    left: 470px;
    top: 0;
    width: 48px;
    height: 100%;
    background: var(--panel-grey);
  }
  .band-panel {
    position: absolute;
    left: 534px;
    top: 0;
    right: 0;
    height: 100%;
    background: var(--panel-grey);
  }
  .person {
    position: absolute;
    left: 560px;
    top: 170px;
    font-family: "Arimo", Arial, sans-serif;
    color: var(--text-light);
  }
  .person-name {
    font-size: 30px;
    font-weight: 700;
    letter-spacing: 1px;
    margin-left: 18px;
  }
  .person-role {
    font-size: 20px;
    margin-top: -4px;
  }
  .contact-icons {
    position: absolute;
    left: 490px;
    top: 278px;
    width: 40px;
    background: var(--card-white);
    padding: 4px 0;
  }
  .contact-icons svg {
    display: block;
    margin: 6px auto;
  }
  .contacts {
    position: absolute;
    left: 556px;
    top: 282px;
    margin: 0;
    padding: 0;
    list-style: none;
    font-family: "Tinos", "Times New Roman", serif;
    font-size: 24px;
    line-height: 34px;
    color: var(--text-light);
    letter-spacing: 0.5px;
  }
</style>
</head>
<body>
<main class="canvas">
  <section class="card" aria-label="Business card">
    <div class="brand">
      <div class="brand-name"><span class="brand-dot"></span>Kelvora Appeals</div>
    </div>

    <div class="band-narrow"></div>
    <div class="band-panel"></div>

    <div class="person">
      <div class="person-name">Rowan Ashby</div>
      <div class="person-role">Director</div>
    </div>

    <div class="contact-icons">
      <svg width="22" height="22" viewBox="0 0 22 22" aria-label="Phone">
        <path d="M3 8 Q11 1 19 8 L16 10 L14 7 L8 7 L6 10 Z" fill="var(--accent-red)"/>
        <rect x="5" y="11" width="12" height="8" rx="1" fill="var(--accent-red)"/>
      </svg>
      <svg width="22" height="22" viewBox="0 0 22 22" aria-label="Email">
        <rect x="2" y="5" width="18" height="12" fill="var(--accent-red)"/>
        <path d="M2 5 L11 12 L20 5" stroke="#fff" stroke-width="1.5" fill="none"/>
      </svg>
      <svg width="22" height="22" viewBox="0 0 22 22" aria-label="Website">
        <rect x="2" y="4" width="18" height="12" fill="none" stroke="var(--accent-red)" stroke-width="2"/>
        <rect x="8" y="17" width="6" height="2" fill="var(--accent-red)"/>
      </svg>
    </div>

    <ul class="contacts">
      <li>0044 7812 305</li>
      <li>info@kelvoraappeals.com</li>
      <li>www.kelvoraappeals.com</li>
    </ul>
  </section>
</main>
</body>
</html>
```